Maralby Information Posters for Student signage

Secondary school looking for some posters to display throughout the school with fresh designs using school colours and fitting with general feel of the school's graphic image. The final designs should be welcoming but clearly outline the required instructions. Sample designs that have been created by the school are attached with the relevant information that is required to appear on the signs. School would like a more dynamic design than the basic signs attached.
We are looking for:
- Large pop-up banner style size for the 2 posters called
"Ready for class" and "Morning Routine".
- Printable poster for the "Maralby Outdoor" sign.

Please incorporate a design feature of "the Maralby 1,2,3" into the posters and also use the Maralby Leaner values of Integrity, Compassion, Curiosity and Drive to help illustrate the content.

An option for design is to incorporate our school's first nations artwork into the design and i have also provided various extracts of design pieces that the school often uses in it's marketing materials.

Target Market(s)

Secondary School Students

Industry/Entity Type

Education

Colors
00AB8E
00BBA5
67D7C9
C6EFE9
E9F9F6
FFF300
FFF600
FEFA6F
FFFEC7
FFFEE8
FFC000
F8CF3A
FAE287
FDF2CF
FEFAEE

Requirements
Must have
• My project must have eyecatching graphics

```html
<!DOCTYPE html>
<html lang="en">
<head>
<meta charset="utf-8">
<title>Maralby Information Posters</title>
<link rel="stylesheet" href="https://fonts.googleapis.com/css2?family=Archivo+Black&family=Poppins:wght@500;600;700&family=Roboto:wght@700&family=Playfair+Display:ital@1&display=swap">
<style>
  :root {
    --stage: #5f5f5f;
    --cream: #efebe4;
    --green-dark: #1b3d1f;
    --green-deep: #12301a;
    --green-mid: #2f6a34;
    --yellow: #ffe600;
    --yellow-soft: #f3e62c;
    --orange: #f26522;
    --red: #e3262c;
    --sky: #9fd0de;
    --olive: #c4bc48;
    --white: #ffffff;
  }
  * { box-sizing: border-box; margin: 0; padding: 0; }
  html, body { width: 1079px; height: 1200px; overflow: hidden; background: var(--stage); }
  .stage { position: relative; width: 1079px; height: 1200px; }

  .banner {
    position: absolute; top: 53px; width: 447px; height: 1085px;
    background: var(--cream); overflow: hidden;
    font-family: "Poppins", sans-serif; color: var(--green-dark);
  }
  .banner--ready { left: 67px; }
  .banner--hats { left: 551px; }

  .banner__artwork-top, .banner__artwork-bottom { position: absolute; left: 0; width: 447px; }
  .banner__artwork-top { top: 0; height: 260px; }
  .banner__artwork-bottom { top: 860px; height: 225px; }

  .title-box {
    position: absolute; left: 70px; top: 101px; width: 306px; height: 133px;
    background: var(--yellow); border-radius: 22px;
  }
  .title-box__name {
    position: absolute; left: 8px; right: 8px; top: 8px; height: 62px;
    background: var(--white); border-radius: 14px 14px 0 0;
    font-family: "Roboto", sans-serif; font-weight: 700; font-size: 42px;
    line-height: 62px; text-align: center; letter-spacing: -0.5px;
  }
  .title-box__steps { position: absolute; left: 0; right: 0; top: 75px; display: flex; justify-content: center; gap: 36px; }
  .step-dot {
    width: 46px; height: 46px; border-radius: 50%;
    border: 2px solid var(--green-dark);
    font-family: "Roboto", sans-serif; font-weight: 700; font-size: 28px;
    color: var(--white); display: flex; align-items: center; justify-content: center;
  }
  .step-dot--one { background: var(--red); }
  .step-dot--two { background: var(--green-dark); }
  .step-dot--three { background: var(--sky); }

  .headline { position: absolute; left: 0; right: 0; text-align: center; font-family: "Archivo Black", sans-serif; line-height: 1; }
  .headline--are-you { top: 277px; font-size: 50px; letter-spacing: 1px; }
  .headline--ready { top: 318px; font-size: 96px; letter-spacing: -1px; }
  .headline--we-wear { top: 282px; font-size: 33px; letter-spacing: 1px; }
  .headline--at-school { top: 312px; font-size: 56px; letter-spacing: -1px; }

  .class-pill {
    position: absolute; left: 43px; top: 416px; width: 363px; height: 55px;
    background: var(--yellow); border-radius: 28px; overflow: hidden;
    font-family: "Archivo Black", sans-serif; display: flex; align-items: center;
  }
  .class-pill__for {
    width: 107px; height: 100%; background: var(--orange); color: var(--white);
    font-size: 34px; display: flex; align-items: center; justify-content: center;
    border-radius: 28px 0 0 28px;
  }
  .class-pill__class { flex: 1; text-align: center; font-size: 50px; padding-right: 30px; }

  .outdoors-pill {
    position: absolute; left: 58px; top: 373px; width: 326px; height: 41px;
    background: var(--yellow); border-radius: 20px;
    font-family: "Archivo Black", sans-serif; font-size: 25px;
    display: flex; align-items: center; justify-content: center; letter-spacing: 0.5px;
  }

  .icon-item { position: absolute; width: 140px; text-align: center; }
  .icon-item__disc {
    margin: 0 auto; border-radius: 50%; background: var(--green-dark);
    border: 6px solid var(--olive); position: relative;
    display: flex; align-items: center; justify-content: center;
  }
  .banner--ready .icon-item__disc { width: 108px; height: 108px; }
  .banner--hats .icon-item__disc { width: 102px; height: 102px; }
  .icon-item__badge {
    position: absolute; left: -10px; top: -8px; width: 31px; height: 31px; border-radius: 50%;
    border: 2px solid var(--white); color: var(--white);
    font-weight: 600; font-size: 15px; display: flex; align-items: center; justify-content: center;
  }
  .icon-item__badge--one { background: var(--red); }
  .icon-item__badge--two { background: var(--green-dark); }
  .icon-item__badge--three { background: var(--sky); color: var(--green-dark); }
  .icon-item__label { font-weight: 600; font-size: 18px; line-height: 1.12; margin-top: 10px; }
  .banner--hats .icon-item__label { font-size: 19px; margin-top: 12px; }
  .icon-item__note { display: block; font-weight: 500; font-size: 10px; margin-top: 3px; }
  .icon-placeholder { width: 56px; height: 62px; border-radius: 10px; background: linear-gradient(160deg, #3c6b40, #24492a); }

  .values-card {
    position: absolute; left: 40px; width: 367px; height: 90px;
    background: var(--white); border-radius: 14px;
    box-shadow: 0 10px 10px -6px rgba(0,0,0,0.35);
  }
  .values-card__title {
    position: absolute; left: 50%; top: -12px; transform: translateX(-50%);
    width: 267px; height: 26px; border-radius: 13px; background: var(--green-dark);
    color: var(--yellow-soft); font-weight: 600; font-size: 16px;
    display: flex; align-items: center; justify-content: center; gap: 5px; white-space: nowrap;
  }
  .values-card__list { position: absolute; top: 27px; list-style: none; font-weight: 600; font-size: 16px; line-height: 24px; }
  .values-card__list--left { left: 48px; }
  .values-card__list--right { left: 206px; }
  .values-card__list li { display: flex; align-items: center; gap: 5px; }
  .values-card__divider { position: absolute; left: 189px; top: 30px; width: 0; height: 46px; border-left: 1px dashed #e2d98a; }

  .school-name {
    position: absolute; left: 30px; top: 868px;
    font-weight: 700; font-size: 19px; line-height: 1.1; color: var(--green-dark);
    display: flex; align-items: center; gap: 8px;
  }
  .school-name__mark { width: 14px; height: 14px; border-radius: 50%; background: var(--yellow); border: 0; }

  .tagline {
    position: absolute; left: 0; right: 0; top: 1043px; text-align: center;
    font-family: "Playfair Display", serif; font-style: italic; font-size: 17px;
    word-spacing: 2px;
  }
  .tagline__word { color: var(--yellow-soft); margin: 0 7px; }
  .tagline__word--light { color: var(--white); }
</style>
</head>
<body>
<main class="stage">

  <!-- Ready for class banner -->
  <section class="banner banner--ready">
    <svg class="banner__artwork-top" viewBox="0 0 447 260" role="img" aria-label="First Nations dot artwork in deep greens with white dotted flowing lines">
      <defs>
        <radialGradient id="topGlowA" cx="0.8" cy="0.2" r="0.7">
          <stop offset="0" stop-color="#3f7a3a"/><stop offset="1" stop-color="#153a1c"/>
        </radialGradient>
      </defs>
      <path d="M0 0H447V205Q300 250 0 245Z" fill="url(#topGlowA)"/>
      <path d="M0 235Q200 205 447 215" fill="none" stroke="#ffffff" stroke-width="3"/>
      <path d="M300 222L447 245V262L300 240Z" fill="var(--yellow)"/>
    </svg>

    <div class="title-box">
      <div class="title-box__name">The Maralby</div>
      <div class="title-box__steps">
        <span class="step-dot step-dot--one">1</span>
        <span class="step-dot step-dot--two">2</span>
        <span class="step-dot step-dot--three">3</span>
      </div>
    </div>

    <h1 class="headline headline--are-you">ARE YOU</h1>
    <p class="headline headline--ready">READY</p>
    <div class="class-pill"><span class="class-pill__for">FOR</span><span class="class-pill__class">CLASS</span></div>

    <div class="icon-item" style="left:20px; top:505px;">
      <div class="icon-item__disc">
        <span class="icon-item__badge icon-item__badge--one">01</span>
        <svg width="60" height="60" viewBox="0 0 60 60" fill="none" stroke="#fff" stroke-width="3" stroke-linejoin="round">
          <rect x="10" y="10" width="40" height="30" rx="3"/>
          <path d="M4 46H56L53 51H7Z"/>
          <path d="M30 16L38 19V26Q38 32 30 35Q22 32 22 26V19Z"/>
          <path d="M26 25L29 28L34 22"/>
        </svg>
      </div>
      <p class="icon-item__label">Laptop/<br>workbook</p>
    </div>

    <div class="icon-item" style="left:158px; top:505px;">
      <div class="icon-item__disc">
        <span class="icon-item__badge icon-item__badge--two">02</span>
        <svg width="60" height="64" viewBox="0 0 60 64" fill="none" stroke="#fff" stroke-width="3" stroke-linejoin="round">
          <rect x="16" y="4" width="30" height="54" rx="5"/>
          <path d="M27 10H35"/>
          <circle cx="31" cy="51" r="2.5"/>
        </svg>
      </div>
      <p class="icon-item__label">Phone<br>in Pouchly</p>
    </div>

    <div class="icon-item" style="left:292px; top:505px;">
      <div class="icon-item__disc">
        <span class="icon-item__badge icon-item__badge--three">03</span>
        <span class="icon-placeholder" role="img" aria-label="School uniform with hat icon"></span>
      </div>
      <p class="icon-item__label">Correct<br>uniform<span class="icon-item__note">(Including hat)</span></p>
    </div>

    <div class="values-card" style="top:714px;">
      <div class="values-card__title">★ Maralby Leaner values ★</div>
      <ul class="values-card__list values-card__list--left">
        <li><svg width="15" height="17" viewBox="0 0 15 17" fill="none" stroke="#1b3d1f" stroke-width="1.4"><path d="M7.5 1L14 3.5V8Q14 13.5 7.5 16Q1 13.5 1 8V3.5Z"/><path d="M4.5 8.5L6.8 10.8L10.5 6.5"/></svg>Integrity</li>
        <li><svg width="15" height="17" viewBox="0 0 15 17" fill="none" stroke="#1b3d1f" stroke-width="1.4"><path d="M7.5 1L14 3.5V8Q14 13.5 7.5 16Q1 13.5 1 8V3.5Z"/><path d="M4.5 8.5L6.8 10.8L10.5 6.5"/></svg>Compassion</li>
      </ul>
      <span class="values-card__divider"></span>
      <ul class="values-card__list values-card__list--right">
        <li><svg width="15" height="17" viewBox="0 0 15 17" fill="none" stroke="#1b3d1f" stroke-width="1.4"><path d="M7.5 1L14 3.5V8Q14 13.5 7.5 16Q1 13.5 1 8V3.5Z"/><path d="M4.5 8.5L6.8 10.8L10.5 6.5"/></svg>Curiosity and</li>
        <li><svg width="15" height="17" viewBox="0 0 15 17" fill="none" stroke="#1b3d1f" stroke-width="1.4"><path d="M7.5 1L14 3.5V8Q14 13.5 7.5 16Q1 13.5 1 8V3.5Z"/><path d="M4.5 8.5L6.8 10.8L10.5 6.5"/></svg>Drive</li>
      </ul>
    </div>

    <svg class="banner__artwork-bottom" viewBox="0 0 447 225" role="img" aria-label="First Nations dot artwork wave in greens with yellow and white flowing bands">
      <defs>
        <radialGradient id="bottomGlowA" cx="0.85" cy="0.7" r="0.7">
          <stop offset="0" stop-color="#3a7536"/><stop offset="1" stop-color="#143a1b"/>
        </radialGradient>
      </defs>
      <path d="M0 70Q150 40 260 40Q360 40 447 10V225H0Z" fill="#ffffff"/>
      <path d="M0 78Q150 50 260 50Q360 50 447 20V225H0Z" fill="url(#bottomGlowA)"/>
      <path d="M190 70Q320 55 447 30" fill="none" stroke="var(--yellow)" stroke-width="7"/>
      <path d="M0 110Q200 60 447 55" fill="none" stroke="#ffffff" stroke-width="2"/>
    </svg>

    <div class="school-name"><span class="school-name__mark"></span>Maralby State High</div>

    <p class="tagline"><span class="tagline__word">Prepared.</span><span class="tagline__word tagline__word--light">Focused.</span><span class="tagline__word">Ready to Learn</span></p>
  </section>

  <!-- Outdoor hats banner -->
  <section class="banner banner--hats">
    <svg class="banner__artwork-top" viewBox="0 0 447 260" role="img" aria-label="First Nations dot artwork in deep greens with white dotted flowing lines">
      <defs>
        <radialGradient id="topGlowB" cx="0.8" cy="0.2" r="0.7">
          <stop offset="0" stop-color="#3f7a3a"/><stop offset="1" stop-color="#153a1c"/>
        </radialGradient>
      </defs>
      <path d="M0 0H447V205Q300 250 0 245Z" fill="url(#topGlowB)"/>
      <path d="M0 235Q200 205 447 215" fill="none" stroke="#ffffff" stroke-width="3"/>
      <path d="M300 222L447 245V262L300 240Z" fill="var(--yellow)"/>
    </svg>

    <div class="title-box">
      <div class="title-box__name">The Maralby</div>
      <div class="title-box__steps">
        <span class="step-dot step-dot--one">1</span>
        <span class="step-dot step-dot--two">2</span>
        <span class="step-dot step-dot--three">3</span>
      </div>
    </div>

    <h1 class="headline headline--we-wear">WE WEAR HATS</h1>
    <p class="headline headline--at-school">AT MARALBY</p>
    <div class="outdoors-pill">WHEN OUTDOORS..</div>

    <div class="icon-item" style="left:20px; top:454px;">
      <div class="icon-item__disc">
        <span class="icon-item__badge icon-item__badge--one">01</span>
        <span class="icon-placeholder" role="img" aria-label="Walking figure wearing a hat icon"></span>
      </div>
      <p class="icon-item__label">Walking</p>
    </div>

    <div class="icon-item" style="left:158px; top:454px;">
      <div class="icon-item__disc">
        <span class="icon-item__badge icon-item__badge--two">02</span>
        <span class="icon-placeholder" role="img" aria-label="Seated figure wearing a hat icon"></span>
      </div>
      <p class="icon-item__label">Sitting</p>
    </div>

    <div class="icon-item" style="left:292px; top:454px;">
      <div class="icon-item__disc">
        <span class="icon-item__badge icon-item__badge--three">03</span>
        <span class="icon-placeholder" role="img" aria-label="Figure playing with a ball wearing a hat icon"></span>
      </div>
      <p class="icon-item__label">Playing</p>
    </div>

    <div class="values-card" style="top:632px;">
      <div class="values-card__title">★ Maralby Leaner values ★</div>
      <ul class="values-card__list values-card__list--left">
        <li><svg width="15" height="17" viewBox="0 0 15 17" fill="none" stroke="#1b3d1f" stroke-width="1.4"><path d="M7.5 1L14 3.5V8Q14 13.5 7.5 16Q1 13.5 1 8V3.5Z"/><path d="M4.5 8.5L6.8 10.8L10.5 6.5"/></svg>Integrity</li>
        <li><svg width="15" height="17" viewBox="0 0 15 17" fill="none" stroke="#1b3d1f" stroke-width="1.4"><path d="M7.5 1L14 3.5V8Q14 13.5 7.5 16Q1 13.5 1 8V3.5Z"/><path d="M4.5 8.5L6.8 10.8L10.5 6.5"/></svg>Compassion</li>
      </ul>
      <span class="values-card__divider"></span>
      <ul class="values-card__list values-card__list--right">
        <li><svg width="15" height="17" viewBox="0 0 15 17" fill="none" stroke="#1b3d1f" stroke-width="1.4"><path d="M7.5 1L14 3.5V8Q14 13.5 7.5 16Q1 13.5 1 8V3.5Z"/><path d="M4.5 8.5L6.8 10.8L10.5 6.5"/></svg>Curiosity and</li>
        <li><svg width="15" height="17" viewBox="0 0 15 17" fill="none" stroke="#1b3d1f" stroke-width="1.4"><path d="M7.5 1L14 3.5V8Q14 13.5 7.5 16Q1 13.5 1 8V3.5Z"/><path d="M4.5 8.5L6.8 10.8L10.5 6.5"/></svg>Drive</li>
      </ul>
    </div>

    <svg class="banner__artwork-bottom" viewBox="0 0 447 225" role="img" aria-label="First Nations dot artwork wave in greens with yellow and white flowing bands">
      <defs>
        <radialGradient id="bottomGlowB" cx="0.85" cy="0.7" r="0.7">
          <stop offset="0" stop-color="#3a7536"/><stop offset="1" stop-color="#143a1b"/>
        </radialGradient>
      </defs>
      <path d="M0 70Q150 40 260 40Q360 40 447 10V225H0Z" fill="#ffffff"/>
      <path d="M0 78Q150 50 260 50Q360 50 447 20V225H0Z" fill="url(#bottomGlowB)"/>
      <path d="M190 70Q320 55 447 30" fill="none" stroke="var(--yellow)" stroke-width="7"/>
      <path d="M0 110Q200 60 447 55" fill="none" stroke="#ffffff" stroke-width="2"/>
    </svg>

    <div class="school-name"><span class="school-name__mark"></span>Maralby State High</div>

    <p class="tagline"><span class="tagline__word">Prepared.</span><span class="tagline__word tagline__word--light">Focused.</span><span class="tagline__word">Ready to Learn</span></p>
  </section>

</main>
</body>
</html>
```